A Billboard Sign - TWO SIGNS

Hi, I’m looking to produce approximately 2.74 m by 2.74 m for a billboard-style display. I have a mock-up of the general look and feel, but I need a more polished, professional design. The sign will be viewed by people driving past, so the messaging must be clear, bold and easily readable at speed.

I also need a second sign sized 1 m by 3 m, following the same branding and visual style as the larger piece.

Requirements
Must have
• It must use the colours I've submitted
Nice to have
• I would like to see some good ideas in the general theme of what I have Mocked up. I don't the same design sent back to me

```html
<!DOCTYPE html>
<html lang="en">
<head>
<meta charset="utf-8">
<title>Northpeak Enterprises – Billboard Signs</title>
<link href="https://fonts.googleapis.com/css2?family=Montserrat:wght@600;700;800;900&display=swap" rel="stylesheet">
<style>
  :root {
    --orange: #f8930f;
    --navy: #1b2a33;
    --white: #ffffff;
    --page: #f2f2f2;
  }
  * { box-sizing: border-box; margin: 0; padding: 0; }
  html, body { width: 936px; height: 1200px; overflow: hidden; }
  body {
    position: relative;
    background: var(--page);
    font-family: "Montserrat", Arial, sans-serif;
    color: var(--navy);
  }

  /* ---------- Square sign 2.74 m x 2.74 m ---------- */
  .sign-square {
    position: absolute;
    left: 18px; top: 350px;
    width: 500px; height: 500px;
    background: var(--orange);
    display: flex; flex-direction: column;
  }
  .sign-square .brand {
    display: flex; align-items: center; gap: 22px;
    padding: 62px 0 0 40px;
  }
  .brand-dot {
    width: 96px; height: 96px; border-radius: 50%;
    background: var(--navy); flex: none;
  }
  .brand-name {
    font-weight: 800; line-height: 1.05; letter-spacing: 1px;
  }
  .sign-square .brand-name { font-size: 38px; }
  .sign-square .message {
    text-align: center; margin-top: 62px; font-weight: 800; line-height: 1;
  }
  .sign-square .award { font-size: 36px; }
  .sign-square .field { font-size: 43px; margin-top: 2px; }
  .sign-square .role {
    font-size: 16px; font-weight: 700; letter-spacing: 6px; margin-top: 4px;
  }
  .sign-square .partner-band {
    margin-top: auto; height: 115px; background: var(--navy); color: var(--white);
    padding: 12px 22px 0;
  }
  .band-label { font-size: 12px; font-weight: 700; letter-spacing: .5px; }
  .sign-square .band-row {
    display: flex; align-items: center; gap: 22px; margin-top: 26px;
  }
  .partner { font-weight: 700; font-size: 15px; }
  .site { font-weight: 700; font-size: 14px; margin-left: auto; letter-spacing: .3px; }

  /* ---------- Tall sign 1 m x 3 m ---------- */
  .sign-tall {
    position: absolute;
    left: 536px; top: 0;
    width: 400px; height: 1200px;
    background: var(--orange);
    display: flex; flex-direction: column; align-items: center;
  }
  .sign-tall .brand-dot { width: 150px; height: 150px; margin-top: 120px; }
  .sign-tall .brand-name {
    font-size: 44px; text-align: center; margin-top: 64px; line-height: 1.25;
  }
  .sign-tall .message {
    margin-top: 120px; text-align: center; font-weight: 900;
    font-size: 37px; line-height: 60px;
  }
  .sign-tall .partner-band {
    margin-top: auto; width: 100%; height: 324px; background: var(--navy);
    color: var(--white); display: flex; flex-direction: column; align-items: center;
  }
  .sign-tall .band-label { font-size: 14px; margin-top: 44px; }
  .sign-tall .band-row { display: flex; gap: 36px; margin-top: 76px; }
  .sign-tall .partner { font-size: 20px; }
  .sign-tall .site { margin: 62px 0 0; font-size: 17px; }
</style>
</head>
<body>

  <section class="sign-square" aria-label="Square billboard sign">
    <div class="brand">
      <span class="brand-dot"></span>
      <div class="brand-name">NORTHPEAK<br>ENTERPRISES</div>
    </div>
    <div class="message">
      <div class="award">AWARD WINNING</div>
      <div class="field">DATA ANALYTICS</div>
      <div class="role">IMPLEMENTATION PARTNER</div>
    </div>
    <div class="partner-band">
      <div class="band-label">PROUDLY PARTNERING WITH</div>
      <div class="band-row">
        <span class="partner">CORVANE</span>
        <span class="partner">Tessaline</span>
        <span class="site">WWW.NORTHPEAKENTERPRISES.IE</span>
      </div>
    </div>
  </section>

  <section class="sign-tall" aria-label="Tall billboard sign">
    <span class="brand-dot"></span>
    <div class="brand-name">NORTHPEAK<br>ENTERPRISES</div>
    <div class="message">
      AWARD WINNING<br>DATA ANALYTICS<br>IMPLEMENTATION<br>PARTNER
    </div>
    <div class="partner-band">
      <div class="band-label">PROUDLY PARTNERING WITH</div>
      <div class="band-row">
        <span class="partner">CORVANE</span>
        <span class="partner">Tessaline</span>
      </div>
      <div class="site">WWW.NORTHPEAKENTERPRISES.IE</div>
    </div>
  </section>

</body>
</html>
```